gracefulgemstore.com.au needs a new web design!

We are after a refurbished web design. gracefulgemstore.com.au is an online jewellery store - it represents a brand that is elegant, graceful and superior in quality.

We have colours that we like but are open to new colour schemes. Our favourite colours are teal and cherry (see attached colour story). We also like simple designs with lots of white space.

A website which we love the layout and design is www.velmora.com.au please try and design in a similar fashion.

We require three important pages:

- Home page
- Tiled product category Page (eg. earrings, see current website)
- Single Product Page.

Please be aware we are limited to the current Content Management System for our website so using similiar (but not limited too) layout would be helpful for the lonely developer (me).

Our designer should provide (at least) photoshop files for our disposal with category headings etc being able to be edited as we add or change new product categories.

We have plans to get large photos of models for the home page in the future, but should also be available for large photos of jewellery. Basically we believe photos are essential to sell our product, so please don't be afraid to incorporate some dummy photos into your design. Especially the home page!

We also offer free shipping Australia Wide, please incorporate this into the home page, product and category pages, it needs to show the visitor that it is specifically Free Australian wide shipping.

Other stuff we need:

A cool shipping info button/box (see current single product page)
Some Social networking buttons/boxes for Chatterly and quipster for possible use on home page.

please email oliver@gracefulgemstore.com.au if you have any questions.

Many thanks and we look forward to reviewing your designs.
Updates

Thankyou all for your designs, I have messaged 4 designs which are the front runners. some have been reuqested to make slight adjustments, others have been asked to submit the other pages as per brief.

Cheers,

Oliver

Target Market(s)

Ladies in Australia between the ages of 25 and 55

Industry/Entity Type

Shipping

Requirements
Must have
• Hovers, actions and transitions and potential drop downs
Should not have
• Norvane motion.

```html
<!DOCTYPE html>
<html lang="en">
<head>
<meta charset="utf-8">
<title>gracefulgemstore.com.au</title>
<link href="https://fonts.googleapis.com/css2?family=Arimo:wght@400;700&family=Yellowtail&display=swap" rel="stylesheet">
<style>
:root{
  --cherry:#d0102a;
  --cherry-deep:#a8061c;
  --teal:#0b7f80;
  --ink:#222;
  --line:#ddd;
  --panel:#f1f1f1;
  --white:#fff;
  --hair:#e9d5ad;
  --skin:#efc3a6;
  --skin-deep:#d89b7f;
  --script:"Yellowtail","Brush Script MT","Segoe Script","Lucida Handwriting",cursive;
}
*{box-sizing:border-box;margin:0;padding:0}
html,body{width:1200px;height:1080px;overflow:hidden;background:var(--white)}
body{font-family:"Arimo",Arial,Helvetica,sans-serif;color:var(--ink)}
a{color:inherit;text-decoration:none;transition:color .2s}
a:hover{color:var(--cherry)}
.page{position:relative;width:1000px;height:900px;transform:scale(1.2);transform-origin:0 0}
.abs{position:absolute}

.top-rule{left:0;top:12px;width:1000px;border-top:1px solid var(--line)}
.bag-tag{left:925px;top:8px;width:55px;height:66px;background:var(--cherry);color:var(--white);text-align:center;font-size:10px;padding-top:8px;line-height:15px;
  clip-path:polygon(0 0,100% 0,100% 92%,93% 100%,86% 92%,79% 100%,71% 92%,64% 100%,57% 92%,50% 100%,43% 92%,36% 100%,29% 92%,21% 100%,14% 92%,7% 100%,0 92%)}
.bag-tag b{font-size:11px}
.bag-tag .count{color:#ffd200}
.header-rule{left:20px;top:87px;width:960px;border-top:2px dotted #e2e2e2}
.brand-name{left:390px;top:68px;width:220px;text-align:center;background:var(--white);color:var(--cherry);font-size:20px;font-weight:700;line-height:36px}
.welcome{left:24px;top:112px;font-size:11px;color:#999}
.welcome a{color:var(--teal)}
.utility-links{right:20px;top:114px;font-size:11px;color:#999;display:flex}
.utility-links a{padding:0 7px;border-left:1px solid var(--line)}
.utility-links a:first-child{border:0}
.utility-links a:last-child{padding-right:0}

.main-nav{left:20px;top:153px;width:960px;height:38px;border-top:2px solid #e6e6e6;border-bottom:1px solid #e6e6e6}
.nav-links{display:flex;gap:22px;font-size:11px;color:#666;line-height:36px}
.search{position:absolute;right:0;top:0;width:277px;height:35px;background:#e8e8e8;padding:4px 5px}
.search-field{display:block;float:left;width:204px;height:27px;background:var(--white);border:1px solid #ddd}
.search-btn{float:right;width:62px;height:27px;background:var(--teal);color:var(--white);font-size:11px;font-weight:700;text-align:center;line-height:27px;transition:background .2s}
.search-btn:hover{background:var(--cherry)}

.hero{left:20px;top:193px;width:960px;height:490px;background:radial-gradient(ellipse at 70% 30%,#f0183a 0%,var(--cherry) 45%,var(--cherry-deep) 100%);overflow:hidden}
.hero-photo{position:absolute;left:110px;top:0;width:420px;height:490px;
  background:linear-gradient(180deg,var(--hair) 0%,#e6cba3 22%,var(--skin) 40%,#f2cdb4 62%,var(--skin-deep) 100%);
  border-radius:0 46% 0 0/0 30% 0 0;
  -webkit-mask-image:linear-gradient(90deg,rgba(0,0,0,.55) 0%,#000 18%,#000 80%,rgba(0,0,0,0) 100%);
  mask-image:linear-gradient(90deg,rgba(0,0,0,.55) 0%,#000 18%,#000 80%,rgba(0,0,0,0) 100%)}
.hero-copy{position:absolute;left:540px;top:122px;width:420px;text-align:center;color:var(--white);font-family:var(--script);line-height:1;text-shadow:0 2px 3px rgba(90,0,10,.35)}
.hero-copy .the{font-size:46px;display:flex;align-items:center;justify-content:center;gap:14px}
.hero-copy .the::before,.hero-copy .the::after{content:"";width:100px;border-top:1px solid rgba(255,255,255,.8)}
.hero-copy .big{font-size:46px;margin-top:4px}
.hero-copy .mid{font-size:36px;margin-top:2px}
.hero-copy .huge{font-size:78px;margin-top:4px}

.promo-shipping{left:20px;top:693px;width:470px;height:82px;background:linear-gradient(180deg,#9fdde6 0%,#52b9c6 60%,#2c98a6 100%);overflow:hidden}
.promo-shipping .free{position:absolute;left:0;top:0;width:0;height:0;border-top:82px solid var(--cherry);border-right:82px solid transparent}
.promo-shipping .free span{position:absolute;left:4px;top:-64px;transform:rotate(-45deg);color:var(--white);font-family:var(--script);font-size:24px}
.promo-shipping .title{position:absolute;left:105px;top:20px;color:var(--white);font-family:var(--script);font-size:36px;text-shadow:0 1px 2px rgba(0,0,0,.35)}

.signup{left:500px;top:693px;width:235px}
.signup h2{font-size:16px;font-weight:700;color:var(--ink)}
.signup p{font-size:11px;color:#888;line-height:14px;margin-top:5px}
.signup-form{display:flex;margin-top:6px;height:22px;border:1px solid #ccc}
.signup-field{flex:1;font-size:11px;color:#333;padding:5px 6px;background:#f7f7f7}
.signup-go{width:24px;background:var(--cherry);color:var(--white);font-size:11px;font-weight:700;text-align:center;line-height:20px}

.questions{left:745px;top:693px;width:235px;height:82px;border:1px solid #cfe9ea;padding:3px;background:var(--white)}
.questions-inner{height:100%;background:linear-gradient(180deg,#c9f0f2,#8fd0d6);padding:4px 12px}
.questions h2{font-weight:400;font-size:25px;color:var(--teal)}
.questions p{font-size:13px;color:var(--teal);line-height:16px;margin-top:4px}

.community{left:20px;top:785px;width:235px;height:72px;background:var(--panel);border:1px solid #e4e4e4;display:flex;align-items:center;gap:14px;padding:0 16px}
.community-label{text-align:center;color:#666;font-size:16px;line-height:17px}
.community-label b{display:block;font-size:13px;letter-spacing:.3px}
.social{display:flex;flex-direction:column;gap:3px;font-size:11px;color:#555}
.social a{display:flex;align-items:center;gap:5px}
.social i{width:8px;height:8px;background:var(--teal);display:inline-block}

.payment{left:265px;top:785px;width:715px;height:72px;border:1px solid #e4e4e4;background:#f3f3f3}
.payment p{position:absolute;left:17px;top:15px;width:420px;font-size:16px;color:#666;line-height:20px}
.payment-methods{position:absolute;right:0;top:0;height:70px;width:268px;background:var(--white);clip-path:polygon(18px 0,100% 0,100% 100%,18px 100%,0 50%);display:flex;align-items:center;justify-content:flex-end;gap:8px;padding-right:14px;font-size:10px;color:#555}
.card{width:48px;height:32px;border:1px solid #ddd;border-radius:3px;display:flex;align-items:center;justify-content:center}

.footer-links{left:20px;top:869px;display:flex;gap:15px;font-size:11px;color:#333}
.copyright{right:20px;top:869px;font-size:11px;color:var(--teal)}
</style>
</head>
<body>
<div class="page">
  <div class="abs top-rule"></div>
  <a class="abs bag-tag" href="#"><b>MY BAG</b><br><span class="count">0</span><br>ITEMS</a>

  <div class="abs header-rule"></div>
  <div class="abs brand-name">gracefulgemstore</div>
  <div class="abs welcome">WELCOME, ( <a href="#">LOG IN</a> )</div>
  <nav class="abs utility-links"><a href="#">ABOUT</a><a href="#">CUSTOMER SERVICE</a><a href="#">CREATE ACCOUNT</a></nav>

  <div class="abs main-nav">
    <nav class="nav-links"><a href="#">EARRINGS</a><a href="#">BRACELETS</a><a href="#">NECKLACES</a><a href="#">CHAINS</a><a href="#">PENDANTS</a></nav>
    <div class="search"><span class="search-field"></span><a class="search-btn" href="#">SEARCH</a></div>
  </div>

  <section class="abs hero">
    <div class="hero-photo" role="img" aria-label="Photo of a smiling blonde model wearing a large diamond cocktail ring"></div>
    <div class="hero-copy">
      <div class="the">The</div>
      <div class="big">Perfect Diamond</div>
      <div class="mid">For Your</div>
      <div class="huge">Valentine!</div>
    </div>
  </section>

  <div class="abs promo-shipping" role="img" aria-label="City harbour skyline photo behind the free shipping message">
    <div class="free"><span>FREE</span></div>
    <div class="title">Shipping Australia Wide</div>
  </div>

  <div class="abs signup">
    <h2>SIGN UP FOR EMAIL</h2>
    <p>Plus, receive a special Welcome Offer just for signing up.</p>
    <div class="signup-form"><span class="signup-field">Enter Email Address</span><a class="signup-go" href="#">GO</a></div>
  </div>

  <div class="abs questions"><div class="questions-inner">
    <h2>Questions</h2>
    <p>Email:<br>oliver@gracefulgemstore.com.au</p>
  </div></div>

  <div class="abs community">
    <div class="community-label">the<b>COMMUNITY</b></div>
    <div class="social"><a href="#"><i></i>quipster</a><a href="#"><i></i>Feed</a><a href="#"><i></i>Chatterly</a></div>
  </div>

  <div class="abs payment">
    <p>Payment is SAFE and EASY we accept the following methods for purchases</p>
    <div class="payment-methods">
      <span class="card">Paywell</span><span class="card">Amberline</span><span class="card">Meridian</span><span class="card">Vistra</span>
    </div>
  </div>

  <nav class="abs footer-links"><a href="#">HOME</a><a href="#">ABOUT US</a><a href="#">GRACEFULGEMSTORE.COM.AU</a><a href="#">GRACEFULGEMSTORE FOR THE PRESS</a><a href="#">CUSTOMER SERVICE</a><a href="#">PRIVACY POLICY</a></nav>
  <div class="abs copyright">© 2012. gracefulgemstore.com.au</div>
</div>
</body>
</html>
```